Thornwell Building Company - advertisement poster

I am looking to print some canvas signs to advertise my general contracting company, Thornwell Building Company. The sign will measure 6' long x 3' high so the size should match that ratio. I already have a logo icon, which is the Letter 'A' and some trees that I would like to incorporate, see attached. I would also like the to have the following information listed:
1) phone number: 472-318-6095
2) email: thornwellbuildingcompany@mailvistra.net
3) website: thornwellbuildingcompany.com
4) Lic#5386204
5) I want to use this text: "BUILD WITH THE T-CREW!"

The ad should be relatively simple and clean. Black and Green are my company colors. I am open to creative ideas!

Target Market(s)

People looking to renovate their homes

Industry/Entity Type

Construction

Colors
59FF00
82FF00
B8FF75
E3FFCB
F4FFEA

Requirements
Must have
• Must have my company logo
Should not have
• No photos or complex graphics

```html
<!DOCTYPE html>
<html lang="en">
<head>
<meta charset="UTF-8">
<title>Thornwell Building Company – Sign</title>
<link href="https://fonts.googleapis.com/css2?family=Archivo+Black&family=Montserrat:wght@400;600;700;800&display=swap" rel="stylesheet">
<style>
  :root {
    --green: #6cb33f;
    --black: #1b1b1b;
    --white: #ffffff;
    --backdrop: #d9dcd6;
  }
  * { margin: 0; padding: 0; box-sizing: border-box; }
  html, body { width: 1200px; height: 800px; overflow: hidden; background: var(--backdrop); }
  .canvas { position: relative; width: 1200px; height: 800px; display: flex; align-items: center; justify-content: center; }
  .sign { position: relative; width: 1200px; height: 600px; display: flex; }
  .sign__slogan {
    width: 690px; height: 100%; background: var(--green);
    display: flex; align-items: center; padding-left: 58px;
  }
  .slogan {
    font-family: "Archivo Black", sans-serif; color: var(--black);
    font-size: 100px; line-height: 0.98; letter-spacing: -1px;
  }
  .slogan__crew { font-size: 112px; }
  .sign__contact {
    width: 510px; height: 100%; background: var(--black);
    display: flex; flex-direction: column; align-items: center;
  }
  .brand { margin-top: 78px; display: flex; flex-direction: column; align-items: center; }
  .brand__mark { width: 48px; height: 48px; background: var(--green); margin-bottom: 18px; }
  .brand__name {
    font-family: "Montserrat", sans-serif; font-weight: 800; color: var(--white);
    text-transform: uppercase; text-align: center; font-size: 34px; line-height: 1.1; letter-spacing: 2px;
  }
  .brand__name small { display: block; font-size: 19px; letter-spacing: 6px; }
  .brand__phone {
    font-family: "Montserrat", sans-serif; font-weight: 700; color: var(--white);
    font-size: 14px; letter-spacing: 3px; margin-top: 12px;
  }
  .tagline {
    font-family: "Montserrat", sans-serif; font-weight: 700; color: var(--white);
    font-size: 14px; letter-spacing: 3px; margin-top: 26px;
  }
  .phone {
    display: flex; align-items: center; gap: 18px; margin-top: 44px;
    font-family: "Montserrat", sans-serif; font-weight: 800; color: var(--white); font-size: 50px; letter-spacing: 1px;
  }
  .phone svg { width: 36px; height: 36px; }
  .email-band {
    width: 100%; background: var(--white); margin-top: 14px; height: 44px;
    display: flex; align-items: center; justify-content: center;
    font-family: "Montserrat", sans-serif; font-weight: 400; color: var(--black); font-size: 17.5px; letter-spacing: 0.5px;
  }
  .website {
    display: flex; align-items: center; gap: 16px; margin-top: 20px;
    font-family: "Montserrat", sans-serif; font-weight: 700; color: var(--green); font-size: 21px;
  }
  .website svg { width: 28px; height: 28px; }
  .license {
    font-family: "Montserrat", sans-serif; font-weight: 600; color: var(--white);
    font-size: 13px; letter-spacing: 2px; margin-top: 18px; opacity: 0.8;
  }
</style>
</head>
<body>
<main class="canvas">
  <section class="sign">
    <div class="sign__slogan">
      <h1 class="slogan">Build<br>with the<br><span class="slogan__crew">T-CREW!</span></h1>
    </div>
    <div class="sign__contact">
      <div class="brand">
        <div class="brand__mark"></div>
        <p class="brand__name">Thornwell<small>Building Company</small></p>
        <p class="brand__phone">472.318.6095</p>
      </div>
      <p class="tagline">JOIN THE T-CREW!</p>
      <p class="phone">
        <svg viewBox="0 0 36 36" aria-hidden="true">
          <circle cx="18" cy="18" r="16" fill="none" stroke="var(--green)" stroke-width="2.5"/>
          <path d="M12.5 10.5c1-.8 2-.6 2.6.4l1.6 2.6c.5.9.3 1.7-.5 2.3l-1 .7c.8 2 2.3 3.6 4.3 4.5l.8-1c.6-.8 1.5-.9 2.3-.4l2.5 1.6c1 .6 1.1 1.7.3 2.6l-1 1.1c-1.3 1.4-4 1-7-1.2-3.3-2.4-5.7-6-5.6-9.1 0-1.7.6-2.9 1.7-4.1z" fill="var(--green)"/>
        </svg>
        472.318.6095
      </p>
      <p class="email-band">thornwellbuildingcompany@mailvistra.net</p>
      <p class="website">
        <svg viewBox="0 0 28 28" aria-hidden="true" fill="none" stroke="var(--green)" stroke-width="2">
          <circle cx="14" cy="14" r="12"/>
          <ellipse cx="14" cy="14" rx="5.5" ry="12"/>
          <line x1="2" y1="14" x2="26" y2="14"/>
          <line x1="4" y1="8" x2="24" y2="8"/>
          <line x1="4" y1="20" x2="24" y2="20"/>
        </svg>
        ThornwellBuildingCompany.com
      </p>
      <p class="license">Lic#5386204</p>
    </div>
  </section>
</main>
</body>
</html>
```